Daily Paid Subscription Newsletter

We need a newsletter design, the details of which are:
What are we doing: We are launching a new paid subscription service targeting marketers, social media agaencies and online publishers.
What will the newsletter content be like: This will contain "content ideas" brands and publishers can use
What is the frequency of the newsletter: This will be a daily newsletter. Not on weekends
Is there a construct of sorts: Yes. There are 3 components to the newsletter. (1) Whats trending today / Hot Today (2) Whats Trending this week / Hot this week and (3) Seasonal Trends / Hot this month
What media formats we need to consider: Text, Images and Videos
What is the name of this newsletter: Plover Suggests (please help in creating this unit with the help of attached logo)
What is being uploaded: (1) A sample day's content for the newsletter in a word doc. Refer to "Plover Suggests Sample & Brief.doc"
Target Market(s)
Social Media Agencies, marketers, publishers. Global market
Industry/Entity Type
Marketing
Colors
Designer to choose colors to be used in the design.
Requirements
Must have
- more text, less visual. this is a paid subscription service. Many stories upfront
Nice to have
- hues of the website. this is WIP but you can refer to plover.co.in to know more
Should not have
- avoid going beyod 2 or max 3 scrolls

```html
<!DOCTYPE html>
<html lang="en">
<head>
<meta charset="utf-8">
<title>Plover Suggests – Daily Newsletter</title>
<link href="https://fonts.googleapis.com/css2?family=Roboto:wght@300;400;500;700&display=swap" rel="stylesheet">
<style>
  :root {
    --page-bg: #d9dcdc;
    --card-bg: #ffffff;
    --brand-blue: #1f5fa8;
    --accent-orange: #f5821f;
    --accent-green: #62d46f;
    --sky: #7fd6f0;
    --text-body: #4f5458;
    --text-muted: #7a7f83;
    --rule: #e2e4e5;
    --rule-warm: #fbe3cc;
  }
  * { box-sizing: border-box; margin: 0; padding: 0; }
  html, body {
    width: 1200px; height: 3327px; overflow: hidden;
    background: var(--page-bg);
    font-family: "Roboto", Arial, sans-serif;
    color: var(--text-body);
  }
  .swatches { position: absolute; top: 40px; left: 528px; display: flex; gap: 13px; }
  .swatch { width: 40px; height: 40px; }
  .swatch--sky { background: var(--sky); }
  .swatch--green { background: var(--accent-green); }
  .swatch--orange { background: var(--accent-orange); }
  .contact-note {
    position: absolute; top: 100px; left: 0; width: 1200px;
    text-align: center; font-size: 19px; color: #333;
  }
  .contact-note a { color: var(--brand-blue); }

  .newsletter {
    position: absolute; left: 193px; top: 153px; width: 814px; height: 3008px;
    background: var(--card-bg);
    border-top: 6px solid var(--brand-blue);
    box-shadow: 0 16px 22px rgba(0,0,0,.12);
    padding: 0 33px;
  }
  .masthead { text-align: center; padding-top: 22px; }
  .masthead__mark {
    width: 86px; height: 86px; border-radius: 50%; margin: 0 auto;
    background: radial-gradient(circle at 40% 40%, #b9ecf7, #ffd9a8 55%, #c6f2c4);
  }
  .masthead__name {
    font-size: 44px; font-weight: 300; color: #3c4145;
    line-height: 50px; margin-top: 8px;
  }
  .masthead__rule { width: 235px; height: 1px; background: #cfd2d4; margin: 6px auto 0; }

  .section-head { text-align: center; padding-top: 4px; }
  .section-head--first { padding-top: 34px; }
  .section-head svg { display: block; margin: 0 auto; }
  .section-head__title {
    font-size: 30px; font-weight: 700; color: var(--accent-orange);
    line-height: 34px; margin-top: 6px; letter-spacing: .3px;
  }
  .section-head__rule { height: 1px; background: var(--rule-warm); margin-top: 6px; margin-bottom: 30px; }

  .topic { margin-bottom: 38px; }
  .topic__title {
    font-size: 19px; font-weight: 700; color: var(--accent-green);
    line-height: 30px; margin-bottom: 12px;
  }
  .ideas { border: 1px solid var(--rule); border-top: none; }
  .ideas__head {
    display: flex; justify-content: space-between; align-items: center;
    height: 38px; background: var(--accent-green); color: #fff;
    font-size: 16px; font-weight: 500; padding: 0 18px 0 33px;
  }
  .ideas__list { list-style: none; padding: 8px 0 10px; }
  .ideas__row {
    display: flex; height: 32px; align-items: center;
    font-size: 16px; padding: 0 18px 0 33px;
  }
  .ideas__idea { flex: 1; }
  .ideas__category { width: 290px; }

  .footer { text-align: center; padding-top: 2px; }
  .footer__social { display: flex; justify-content: center; gap: 6px; }
  .footer__social span { width: 36px; height: 36px; border: 2px solid #9a9ea1; border-radius: 50%; }
  .footer__line { font-size: 16px; color: var(--text-muted); line-height: 24px; }
  .footer__phone { margin-top: 12px; }
  .footer__copy { margin-top: 9px; }
</style>
</head>
<body>
  <div class="swatches">
    <span class="swatch swatch--sky"></span>
    <span class="swatch swatch--green"></span>
    <span class="swatch swatch--orange"></span>
  </div>
  <p class="contact-note">For anything about this mail you can contract us by <a href="#">click this link.</a></p>

  <main class="newsletter">
    <header class="masthead">
      <div class="masthead__mark"></div>
      <div class="masthead__name">plover</div>
      <div class="masthead__rule"></div>
    </header>

    <section>
      <div class="section-head section-head--first">
        <svg width="40" height="40" viewBox="0 0 40 40" fill="none" stroke="#f5821f" stroke-width="2.4" stroke-linejoin="round">
          <rect x="6" y="14" width="28" height="22"/><path d="M3 8h34v6H3z"/><path d="M20 8v28M20 8c-4-6-11-6-9-1M20 8c4-6 11-6 9-1"/>
        </svg>
        <h2 class="section-head__title">HOT TODAY</h2>
        <div class="section-head__rule"></div>
      </div>

      <article class="topic">
        <h3 class="topic__title">Fake cash dispensed from CBX ATM</h3>
        <div class="ideas">
          <div class="ideas__head"><span>Content Idea/s:</span><span>Recommended For / Relevant Category</span></div>
          <ul class="ideas__list">
            <li class="ideas__row"><span class="ideas__idea">Guide to identifying real notes</span><span class="ideas__category">Banking / Cashless / Insurance</span></li>
            <li class="ideas__row"><span class="ideas__idea">What to do if you find yourself with fake cash</span><span class="ideas__category">Banking / Security / Government</span></li>
            <li class="ideas__row"><span class="ideas__idea">Yet another reason to go cashless</span><span class="ideas__category">Cashless / Banking / Credit Cards</span></li>
          </ul>
        </div>
      </article>

      <article class="topic">
        <h3 class="topic__title">Lay offs in Cartwave</h3>
        <div class="ideas">
          <div class="ideas__head"><span>Content Idea/s:</span><span>Recommended For / Relevant Category</span></div>
          <ul class="ideas__list">
            <li class="ideas__row"><span class="ideas__idea">Apps to monitor money spending</span><span class="ideas__category">Mobile / Finance</span></li>
            <li class="ideas__row"><span class="ideas__idea">How your phone can help you make money</span><span class="ideas__category">Mobile / Job Sites</span></li>
            <li class="ideas__row"><span class="ideas__idea">Apps that can help you keep updated with jobs</span><span class="ideas__category">Job Sites / Education</span></li>
            <li class="ideas__row"><span class="ideas__idea">How to spend your sabbatical without feeling jobless</span><span class="ideas__category">Travel / Job Sites</span></li>
            <li class="ideas__row"><span class="ideas__idea">Can't afford new clothes? Try these DIY Hacks</span><span class="ideas__category">E-Commerce / Lifestyle / Retail</span></li>
            <li class="ideas__row"><span class="ideas__idea">How to look sharp at your next interview</span><span class="ideas__category">Job Sites / Retail</span></li>
          </ul>
        </div>
      </article>

      <article class="topic">
        <h3 class="topic__title">Lights Off Hour</h3>
        <div class="ideas">
          <div class="ideas__head"><span>Content Idea/s:</span><span>Recommended For / Relevant Category</span></div>
          <ul class="ideas__list">
            <li class="ideas__row"><span class="ideas__idea">3 Reasons to ditch your four wheeler</span><span class="ideas__category">Bikes / Scooters / Auto Finance</span></li>
          </ul>
        </div>
      </article>

      <article class="topic">
        <h3 class="topic__title">Ultra man- Rohan Mehra</h3>
        <div class="ideas">
          <div class="ideas__head"><span>Content Idea/s:</span><span>Recommended For / Relevant Category</span></div>
          <ul class="ideas__list">
            <li class="ideas__row"><span class="ideas__idea">RohanMehra asks #WhyStopHere</span><span class="ideas__category">Bikes / F&amp;B</span></li>
            <li class="ideas__row"><span class="ideas__idea">Running till the end</span><span class="ideas__category">F&amp;B / Pharma / Batteries</span></li>
            <li class="ideas__row"><span class="ideas__idea">Think about the long run</span><span class="ideas__category">Finance</span></li>
            <li class="ideas__row"><span class="ideas__idea">Healthy food is the first step to running a marathon</span><span class="ideas__category">F&amp;B / Sport Equipment</span></li>
            <li class="ideas__row"><span class="ideas__idea">Make things last longer</span><span class="ideas__category">Batteries / Home Improvement</span></li>
          </ul>
        </div>
      </article>

      <article class="topic">
        <h3 class="topic__title">Jay Brenner Concert Tickets price</h3>
        <div class="ideas">
          <div class="ideas__head"><span>Content Idea/s:</span><span>Recommended For / Relevant Category</span></div>
          <ul class="ideas__list">
            <li class="ideas__row"><span class="ideas__idea">10things to do with your money instead of JB tickets</span><span class="ideas__category">E-Commerce / Finance</span></li>
            <li class="ideas__row"><span class="ideas__idea">How to save up for the next big bang concert</span><span class="ideas__category">Finance</span></li>
            <li class="ideas__row"><span class="ideas__idea">What to wear to the JB concert</span><span class="ideas__category">Retail / Fashion</span></li>
          </ul>
        </div>
      </article>

      <article class="topic">
        <h3 class="topic__title">Nimbus Net is about to make data chargeable</h3>
        <div class="ideas">
          <div class="ideas__head"><span>Content Idea/s:</span><span>Recommended For / Relevant Category</span></div>
          <ul class="ideas__list">
            <li class="ideas__row"><span class="ideas__idea">What to do while your data is still free?</span><span class="ideas__category">Mobile / Telecom</span></li>
            <li class="ideas__row"><span class="ideas__idea">You're about to spend a lot more on data. Don't go broke</span><span class="ideas__category">Mobile / Finance</span></li>
          </ul>
        </div>
      </article>

      <article class="topic">
        <h3 class="topic__title">Malik having an objection to 70s song being repurposed</h3>
        <div class="ideas">
          <div class="ideas__head"><span>Content Idea/s:</span><span>Recommended For / Relevant Category</span></div>
          <ul class="ideas__list">
            <li class="ideas__row"><span class="ideas__idea">Some things are meant to stay in the past</span><span class="ideas__category">Consumer durables</span></li>
            <li class="ideas__row"><span class="ideas__idea">7 Reasons why the 70s were the best time for fashion</span><span class="ideas__category">Retail / Ecommerce</span></li>
          </ul>
        </div>
      </article>
    </section>

    <section>
      <div class="section-head">
        <svg width="44" height="40" viewBox="0 0 44 40" fill="none" stroke="#f5821f" stroke-width="2.4" stroke-linejoin="round" stroke-linecap="round">
          <path d="M2 4h6l5 24h24"/><rect x="14" y="6" width="22" height="16"/><path d="M21 6v6h8V6"/><circle cx="16" cy="34" r="3"/><circle cx="33" cy="34" r="3"/>
        </svg>
        <h2 class="section-head__title">HOT THIS WEEK</h2>
        <div class="section-head__rule"></div>
      </div>

      <article class="topic">
        <h3 class="topic__title">Exams</h3>
        <div class="ideas">
          <div class="ideas__head"><span>Content Idea/s:</span><span>Recommended For / Relevant Category</span></div>
          <ul class="ideas__list">
            <li class="ideas__row"><span class="ideas__idea">Superfoods to eat during exams</span><span class="ideas__category">F&amp;b / Health / Pharma</span></li>
            <li class="ideas__row"><span class="ideas__idea">How to not let your child get exhausted during exams</span><span class="ideas__category">Education / Pharma</span></li>
          </ul>
        </div>
      </article>

      <article class="topic">
        <h3 class="topic__title">Exams</h3>
        <div class="ideas">
          <div class="ideas__head"><span>Content Idea/s:</span><span>Recommended For / Relevant Category</span></div>
          <ul class="ideas__list">
            <li class="ideas__row"><span class="ideas__idea">How much gold is in the Golden Reel statue?</span><span class="ideas__category">Finance / Jewelery</span></li>
            <li class="ideas__row"><span class="ideas__idea">How to live like a celebrity?</span><span class="ideas__category">Retail / Lifestyle</span></li>
          </ul>
        </div>
      </article>
    </section>

    <section>
      <div class="section-head">
        <svg width="40" height="40" viewBox="0 0 40 40" fill="none" stroke="#f5821f" stroke-width="2.4" stroke-linejoin="round">
          <path d="M4 12l16-8 16 8v18l-16 8-16-8z"/><path d="M4 12l16 8 16-8M20 20v18"/>
        </svg>
        <h2 class="section-head__title">HOT THIS MONTH</h2>
        <div class="section-head__rule"></div>
      </div>

      <article class="topic">
        <h3 class="topic__title">Summer</h3>
        <div class="ideas">
          <div class="ideas__head"><span>Content Idea/s:</span><span>Recommended For / Relevant Category</span></div>
          <ul class="ideas__list">
            <li class="ideas__row"><span class="ideas__idea">Mocktail recipes to keep you cool?</span><span class="ideas__category">F&amp;B / Retail</span></li>
            <li class="ideas__row"><span class="ideas__idea">How to deal with high humidity?</span><span class="ideas__category">Air Conditioners / Fans</span></li>
            <li class="ideas__row"><span class="ideas__idea">The best shades of whites this summer</span><span class="ideas__category">Fashion / Retail</span></li>
          </ul>
        </div>
      </article>
    </section>

    <footer class="footer">
      <div class="footer__social"><span></span><span></span><span></span></div>
      <p class="footer__line footer__phone">555-014-0192</p>
      <p class="footer__line">support@plovermail.com</p>
      <p class="footer__line footer__copy">© 2017 Plover .</p>
    </footer>
  </main>
</body>
</html>
```